Quillfern Nightclub Flyer (Updated)

Flyer for facebook, square is fine, or rectangular. Here is the text:
QUILLFERN
Nightclub + Lounge
presents

SPLIT DECK WEDNESDAY
Nov 29 2018

CLUB FLOOR:
GORDY B2B RALPH
THEODORE BRUSKVIK

LOUNGE:
OTIS B2B HALF TIDE
COPPER FENWICK

Powered by HALVERN Acoustics
4716 Larchmere Avenue 21+ 9pm-2am
quillfernvenue-example.com for VIP booth inquiries

Target Market(s)

Nightclub

Industry/Entity Type

Night Club

Font styles to use
Sans Serif

Colors

Designer to choose colors to be used in the design.

Requirements
Must have
• All the text listed, and plz keep the theme of the attached files. We want to stay consistent with the Quillfern brand
Nice to have
• Try to stay with the theme from the attachments
Should not have
• Dont' stray to far from the general theme we have from the attachments

```html
<!DOCTYPE html>
<html lang="en">
<head>
<meta charset="utf-8">
<title>Quillfern Nightclub – Split Deck Wednesday</title>
<link rel="stylesheet" href="https://fonts.googleapis.com/css2?family=Montserrat:wght@400;500;600;700&family=Playfair+Display:wght@400;700&display=swap">
<style>
  :root {
    --page: #f4f4f4;
    --card: #faf9f4;
    --card-tint: #f1efe6;
    --ink: #2b2b2b;
    --gold: #b9a41f;
    --gold-deep: #6e6519;
    --gold-light: #d8d27a;
    --frame: #b7a875;
    --vip-bg: #7a6b1e;
    --white: #ffffff;
  }
  * { margin: 0; padding: 0; box-sizing: border-box; }
  html, body { width: 1000px; height: 1200px; overflow: hidden; background: var(--page); }
  .canvas { position: relative; width: 1000px; height: 1200px; }

  .flyer {
    position: absolute; left: 115px; top: 250px; width: 787px; height: 787px;
    background: var(--card);
    font-family: "Montserrat", sans-serif; color: var(--ink); text-align: center;
  }
  .flyer__pattern {
    position: absolute; inset: 0;
    background: radial-gradient(circle at 50% 45%, var(--card) 0%, var(--card-tint) 100%);
  }
  .flyer__frame { position: absolute; inset: 0; }

  .brand-mark {
    position: absolute; left: 329px; top: 13px; width: 124px; height: 124px;
    border-radius: 50%; background: var(--gold-light);
  }
  .brand-name {
    position: absolute; left: 0; right: 0; top: 158px;
    font-family: "Playfair Display", serif; font-weight: 400;
    font-size: 58px; letter-spacing: 2px; line-height: 1; color: var(--ink);
  }
  .brand-tagline {
    position: absolute; left: 0; right: 0; top: 236px;
    font-size: 17px; letter-spacing: 2px; font-weight: 500;
  }
  .presents {
    position: absolute; left: 0; right: 0; top: 270px;
    display: flex; justify-content: center; align-items: center; gap: 14px;
    font-size: 21px; letter-spacing: 1.5px;
  }
  .presents__ornament {
    display: inline-block; width: 20px; height: 22px; background: var(--ink); border-radius: 3px;
  }
  .event-title {
    position: absolute; left: 0; right: 0; top: 318px;
    font-family: "Playfair Display", serif; font-weight: 700;
    font-size: 104px; line-height: 1.1; letter-spacing: 1px;
    background: linear-gradient(180deg, var(--gold-deep) 0%, var(--gold) 100%);
    -webkit-background-clip: text; background-clip: text; color: transparent;
  }
  .event-day {
    position: absolute; left: 0; right: 0; top: 455px;
    font-size: 33px; font-weight: 700; letter-spacing: 2px; color: var(--gold-deep);
  }
  .event-date {
    position: absolute; left: 0; right: 0; top: 498px;
    font-size: 22px; letter-spacing: 2px;
  }
  .event-address {
    position: absolute; left: 0; right: 0; top: 537px;
    font-size: 20px; letter-spacing: 1px; font-weight: 500;
  }
  .event-hours {
    position: absolute; left: 0; right: 0; top: 565px;
    font-size: 25px; font-weight: 700; letter-spacing: 1px; color: var(--gold);
  }
  .vip-label {
    position: absolute; left: 290px; top: 602px; width: 215px; height: 34px;
    background: var(--vip-bg); color: var(--white);
    font-size: 18px; font-weight: 600; line-height: 34px;
  }
  .website {
    position: absolute; left: 0; right: 0; top: 641px;
    font-size: 18px; letter-spacing: 0.5px;
  }

  .lineup {
    position: absolute; left: 0; right: 0; top: 676px; height: 84px;
    display: grid; grid-template-columns: 300px 188px 299px;
  }
  .lineup__room {
    font-size: 15px; font-weight: 600; letter-spacing: 1px; line-height: 23px; padding-top: 15px;
  }
  .sponsor { border-left: 2px solid var(--ink); border-right: 2px solid var(--ink); padding-top: 4px; }
  .sponsor__label { font-size: 15px; font-weight: 600; letter-spacing: 1.5px; }
  .sponsor__name { font-size: 24px; font-weight: 700; letter-spacing: 1px; line-height: 1.2; margin-top: 6px; }
  .sponsor__sub { font-size: 15px; font-weight: 700; letter-spacing: 1px; }
</style>
</head>
<body>
<main class="canvas">
  <article class="flyer">
    <div class="flyer__pattern" role="img" aria-label="Faint cream damask pattern background"></div>
    <svg class="flyer__frame" width="787" height="787" viewBox="0 0 787 787" aria-hidden="true">
      <polyline points="315,31 13,31 13,779 769,779 769,31 473,31" fill="none" stroke="var(--frame)" stroke-width="2.5"/>
    </svg>

    <div class="brand-mark" aria-hidden="true"></div>
    <h1 class="brand-name">QUILLFERN</h1>
    <p class="brand-tagline">NIGHTCLUB + LOUNGE</p>
    <p class="presents">
      <span class="presents__ornament" role="img" aria-label="Small fleur-de-lis ornament"></span>
      PRESENTS
      <span class="presents__ornament" role="img" aria-label="Small fleur-de-lis ornament"></span>
    </p>

    <h2 class="event-title">SPLIT DECK</h2>
    <p class="event-day">WEDNESDAY</p>
    <p class="event-date">NOV | 29 | 2018</p>
    <p class="event-address">4716 LARCHMERE AVENUE 21+</p>
    <p class="event-hours">9PM-2AM</p>
    <p class="vip-label">VIP booth inquiries</p>
    <p class="website">quillfernvenue-example.com</p>

    <section class="lineup">
      <div class="lineup__room">CLUB FLOOR:<br>GORDY B2B RALPH<br>THEODORE BRUSKVIK</div>
      <div class="sponsor">
        <p class="sponsor__label">POWERED BY</p>
        <p class="sponsor__name">HALVERN</p>
        <p class="sponsor__sub">ACOUSTICS</p>
      </div>
      <div class="lineup__room">LOUNGE:<br>OTIS B2B HALF TIDE<br>COPPER FENWICK</div>
    </section>
  </article>
</main>
</body>
</html>
```